App Design Project

OVERVIEW: I want to re-style an iPhone app that is lifestyle orientated for young adults – aged 18-35, male AND female. – to make it more hip, slick, playful with a more dramatic home page and some added styling for other key pages. There is a splash page that users first see, a home page, and about 6-7 other pages for the rest of the app. As well, I want to re-do my app icon that is a memorable design in the icon box shape.

STYLING OF APP PAGES: I am refining a pre-built iPhone application It needs to be hip, stylish, a bit playful, and have a bit of slickness to it. It should be a bit SENSUAL and elegant – but NOT erotic in tone. It already has all pages generally done – the background colors are close and general button positions are completed. The buttons could change in style. The “home” page for the app could have just the bottom buttons- not the 3 in the middle that choose games, news, info. and a dramatic illustration for the rest of the page – with some copy here and there. Now it needs some styling to make it more cool looking and relate to young adults, aged 18-35. It looks nice but a bit flat and plain and, I want to style it more. I want to create a dramatic style with more of a signature to the look.

For the app pages, I would like to:
Backgrounds: See if we can give them a bit more drama, gloss.
Home page: Create an illustrated style - perhaps using silouettes, or line drawaings or high-con imagery in a color – want to be stylish, elegant. It is a a lifestyle app for young adults, so it should speak to socially active, in the know, young adults.
Other key pages: This can play off the home page styling. All buttons on the other pages stay where they are. The backgrounds can be given a bit more gloss – if you like. The tops of the pages can echo the home page with some design related to young adults.
But am open to other styling that can help make it more elegant, edgy, and appealing to young adults. The background colors are nice but maybe a bit flat – may need more of a sense of highlights / gloss to make them pop more.

The BrightPulse logo at the top middle could change, though, if something better comes along. If it stays the same, that’s OK too.

APP ICON: Finally, I want to also create a companion iPhone icon for the app that reflects what is done to style the app itself. I have a dimensional background for the icon and an idea to create a strong, simple element using dual letter S’s – representing the name of the app. The name of the app is two words, each starting with S. The icon should be dramatic, simple, and dimensional in visual tone. It could be as simple as 2 S’s kissing – but it has to be memorable.

ASSETS: I am including about 4 - app frames, including the home page, that could benefit from added styling. Some pages have some opening copy that is in the art.. that will stay in most cases. But they could use some added styling and highlighting. It could be young men’s and women’s faces, graphic elements, or even some aspect of the double S logo/icon look.
Updates

On this project I am looking for the use of the backgrounds I uploaded - especially the home page - but without the three center buttons - easy to take off in the PSD file. Then, I'd like to see some representation of young adult faces or face body in a stylized, abstract way. Not as a realistic image.  So, they may be line drawings in a complementary color - or a high-con of the image in a complementary color. The home page needs to set the style for young adults for the rest of the app. I've uploaded images of young adult people / faces and even some silhouettes that could be used to do a styling of the home page - where the page has buttons top and bottom but a center space with some stylized hip young adult imagery. Not too busy but elegant/edgy. 

Reason: I both want more designers to have a chance to participate and I have added more refined instructions for everyone.

Reason: Had to be out of town for the holiday and thought it was the 27th. Oops. I'll be going through the new designs in detail - communicating with a few of the designers and selecting one of the designers by no later than this coming Friday. Pardon the mistake. I'm new to this. Also, I'm going to up the price a bit about $100. Derek Wansford (628.507.2291)

Reason: I have to be out of town and just got back and need to review new designs. Thank you. Derek

Target Market(s)

Socially active, hip young adults 18-35.

Industry/Entity Type

Games

Requirements
Must have
• Should appeal to socially active young adults and have a strong, elegant design geared toboth male and female users.
Should not have
• This is a fun, educational app – so, it should not be erotic – only stylish, a bit edgy, and a bit sensual.

```html
<!DOCTYPE html>
<html lang="en">
<head>
<meta charset="utf-8">
<title>BrightPulse – App Screens</title>
<link href="https://fonts.googleapis.com/css2?family=PT+Sans:wght@400;700&display=swap" rel="stylesheet">
<style>
  :root {
    --page-bg: #e3ddd8;
    --bar-dark: #141414;
    --bar-mid: #2a2a2a;
    --bar-light: #4a4a4a;
    --home-red: #a5141a;
    --home-red-deep: #6e0c10;
    --home-red-glow: #d9242a;
    --quiz-orange: #e79a2a;
    --quiz-orange-light: #f2b545;
    --quiz-orange-deep: #d57a1c;
    --teal: #2a8f8f;
    --teal-light: #47b0ad;
    --teal-deep: #1b6466;
    --button-text: #f5ecd0;
    --logo-blue: #6cb4c6;
    --tab-text: #c9c9c9;
    --white: #ffffff;
  }
  * { box-sizing: border-box; margin: 0; padding: 0; }
  html, body {
    width: 1200px; height: 827px; overflow: hidden;
    background: var(--page-bg);
    font-family: "PT Sans", sans-serif;
  }
  .screen {
    position: absolute; top: 91px;
    width: 451px; height: 674px;
    overflow: hidden;
    box-shadow: 0 6px 18px rgba(0,0,0,.35);
  }
  .screen--home { left: 114px; background: radial-gradient(ellipse at 60% 60%, var(--home-red-glow) 0%, var(--home-red) 45%, var(--home-red-deep) 100%); }
  .screen--quiz { left: 590px; background: radial-gradient(ellipse at 40% 30%, var(--quiz-orange-light) 0%, var(--quiz-orange) 55%, var(--quiz-orange-deep) 100%); }

  .top-bar {
    position: absolute; left: 0; top: 0; width: 100%; height: 92px;
    background: linear-gradient(to bottom, var(--bar-dark) 0%, var(--bar-dark) 30%, var(--bar-light) 34%, var(--bar-mid) 60%, var(--bar-dark) 100%);
    border-bottom: 1px solid #000;
  }
  .brand {
    position: absolute; left: 50%; top: 42px; transform: translateX(-50%);
    height: 38px; padding: 0 16px;
    display: flex; align-items: center; gap: 8px;
    font-size: 30px; font-weight: 400; letter-spacing: 1px;
    color: var(--logo-blue);
  }
  .brand__square { width: 14px; height: 14px; background: var(--logo-blue); }
  .back-button {
    position: absolute; left: 16px; top: 48px; width: 73px; height: 27px;
    border: 1px solid #777; border-radius: 4px;
    background: linear-gradient(#3a3a3a, #0e0e0e);
    color: var(--white); font-size: 14px; letter-spacing: 1px;
    display: flex; align-items: center; justify-content: center;
  }

  .home-intro {
    position: absolute; left: 0; top: 106px; width: 100%;
    text-align: center; color: var(--white); text-transform: uppercase;
  }
  .home-intro__title { font-size: 19px; font-weight: 700; margin-bottom: 12px; letter-spacing: .5px; }
  .home-intro__text { font-size: 15px; line-height: 22px; letter-spacing: .3px; }
  .home-art {
    position: absolute; left: 25px; top: 219px; width: 418px; height: 386px;
    background: radial-gradient(ellipse at 45% 55%, rgba(230,70,70,.55) 0%, rgba(150,20,25,.6) 45%, rgba(165,20,26,0) 75%);
  }

  .quiz-intro {
    position: absolute; left: 22px; top: 108px; width: 410px;
    color: var(--white); font-size: 16px; line-height: 21px;
  }
  .quiz-button {
    position: absolute; left: 27px; width: 399px; height: 82px;
    border-radius: 14px;
    background: linear-gradient(to bottom, var(--teal-light) 0%, var(--teal) 50%, var(--teal-deep) 100%);
    box-shadow: 0 3px 8px rgba(120,40,0,.55), inset 0 1px 0 rgba(255,255,255,.35);
    display: flex; align-items: center; justify-content: center;
    color: var(--button-text); font-size: 29px; letter-spacing: 2px;
    text-shadow: 0 2px 3px rgba(0,0,0,.5);
  }
  .quiz-button--all { top: 245px; }
  .quiz-button--myths { top: 363px; }
  .quiz-button--health { top: 482px; }

  .tab-bar {
    position: absolute; left: 0; bottom: 0; width: 100%; height: 69px;
    display: flex;
    background: linear-gradient(to bottom, #3d3d3d 0%, #1c1c1c 50%, #0c0c0c 100%);
    border-top: 1px solid #000;
  }
  .tab-bar__item {
    flex: 1; display: flex; align-items: center; justify-content: center;
    color: var(--tab-text); font-size: 14px; letter-spacing: .5px;
    border-right: 1px solid #050505; box-shadow: inset -1px 0 0 #3a3a3a;
  }
  .tab-bar__item:last-child { border-right: 0; box-shadow: none; }
</style>
</head>
<body>
  <section class="screen screen--home">
    <header class="top-bar">
      <div class="brand"><span class="brand__square"></span>BRIGHTPULSE</div>
    </header>
    <div class="home-intro">
      <h1 class="home-intro__title">Your Lifestyle Pro</h1>
      <p class="home-intro__text">Sex news, games, essential information,<br>key links and a sexy poll.<br>Become sex smart and share with others.</p>
    </div>
    <div class="home-art" role="img" aria-label="Glowing red silhouette of a man carrying a woman in his arms"></div>
    <nav class="tab-bar">
      <span class="tab-bar__item">GAMES</span>
      <span class="tab-bar__item">NEWS</span>
      <span class="tab-bar__item">INFO</span>
      <span class="tab-bar__item">POLLS</span>
      <span class="tab-bar__item">ABOUT</span>
    </nav>
  </section>

  <section class="screen screen--quiz">
    <header class="top-bar">
      <span class="back-button">BACK</span>
      <div class="brand"><span class="brand__square"></span>BRIGHTPULSE</div>
    </header>
    <p class="quiz-intro">Test your sex smarts with a quiz! Select a game. After each Q&amp;A, SHAKE your phone for the next question. Answer five questions and see your score! Share your score.</p>
    <div class="quiz-button quiz-button--all">ALL ABOUT SEX</div>
    <div class="quiz-button quiz-button--myths">SEX MYTHS</div>
    <div class="quiz-button quiz-button--health">SEX HEALTH</div>
    <nav class="tab-bar">
      <span class="tab-bar__item">GAMES</span>
      <span class="tab-bar__item">NEWS</span>
      <span class="tab-bar__item">INFO</span>
      <span class="tab-bar__item">POLLS</span>
      <span class="tab-bar__item">ABOUT</span>
    </nav>
  </section>
</body>
</html>
```